"Web Design" E-commerce web site * give me the BEST Equipment website

We require an
Truely EYE catching E-COMMERCE website “Torchline Supplies Australia”
Branded as TSA

**** ARE YOU UP TO THE CHALLENGE !!!! ***

We already have 2 website names registered :
www.torchlinegear.com.au and www.torchlinesuppliesaustralia.com.au
( one is active but unfinished)

If you need to see what will APPEAL TO ME "The two websites below have a lot of what I am looking for (design Style ) www.quorvashop.com & www.plendathemes.com/live/?theme=voranelle
Therefore -a combination of these two sites best features would be very close. !
please use and index with similar catergories to: www.torchlinesuppliesaustralia.com.au

CONCEPT OF SITE
Customer places order through transaction system.. -all payment methods
 which immediately send order through to my own staff and or the respective supplier. (Option for site administrator to choose for each product listing who receives such email)
 Product listings must be easily edited / updated and or replaced by personell with limited computer knowledge (if they can use chatterbox or pagenest they should be able to edit product listings) simply put they will need NO CODE EDITING SKILLS REQUIRED.

Please create a pages for atleast the following:
Main home page
 Harrowby products only
 Fusemark products only
 Vantor products only
 Arcstead products only
 Electrical supplies
 Power Distribution
 Mine spec’d equipment specials
2nd hand equipment
contact
about us
sitemap

Information to populate fields with in pages can be source from our suppliers own websites as we are authorised distributors of the following sites:

http://www.harrowbypower.com.au/catalogue/page3/category1
http://www.fusemark.com.au/product-category/welding-machines/
http://www.arcstead.com.au/products/
http://www.vantor.com

concept:
Basically, the website is to be for the fast movement of stock from Our own stock and Our suppliers – direct to the customers address (drop shipping) with very LIMITED INTERACTION with our customers (email only)
Updates

           SEE IMAGES IN ATTACHED RAR    

ALSO CHECK OUT THESE SITES WHICH SHOW THE STYLES I LIKE  SO THEY WILL HELP YOU DESIGN SOMETHING THAT GETS CLOSER TO MY IDEAL SITE AND MY REQUIREMENTS

we are currently running a poll and will make a decision very shortly.. thanks to all

Target Market(s)

Males 20 to 55
engineering and handyman

Industry/Entity Type

Computer

Requirements
Must have
• That wow factor.. grabs your attention not through tacky.. but well designed / layout
Ease of editing / updating

shipping and freight calculator that automatically adds to invioce

NON compulsory Newsletter - although if customers provide validation of email they receive 2.5% discount on purchases (enter a code sent to them)

the rest is just simple.. amaze me with your talents
Nice to have
• Todays quick sales - campaign
Weekly quick sales - campaign

highlight specials

```html
<!DOCTYPE html>
<html lang="en">
<head>
<meta charset="utf-8">
<title>Torchline Supplies Australia</title>
<link rel="stylesheet" href="https://fonts.googleapis.com/css2?family=Oswald:wght@300;400&family=Arimo:wght@400&display=swap">
<style>
:root{
  --orange:#f26522;
  --orange-dark:#d9531a;
  --ink:#2b2b2b;
  --grey:#666;
  --line:#dcdcdc;
  --green:#4a9a2c;
  --black:#0d0d0d;
  --price:#e0461a;
  --banner-a:#ffd84a;
  --banner-b:#f6a81c;
}
*{box-sizing:border-box;margin:0;padding:0}
html,body{width:929px;height:1200px;overflow:hidden;background:#fff}
body{position:relative;font-family:"Arimo",Arial,sans-serif;color:var(--ink)}
.topbar{position:absolute;left:0;top:0;width:929px;height:22px;background:var(--black);
  display:flex;justify-content:flex-end;gap:25px;padding-right:20px;align-items:center}
.topbar a{color:#fff;font-family:"Oswald",sans-serif;font-size:10.5px;letter-spacing:1px;text-decoration:none;white-space:nowrap}
.masthead{position:absolute;left:0;top:22px;width:929px;height:90px;
  background:linear-gradient(#fff,#e9e9e9);border-bottom:1px solid #d0d0d0}
.brand{position:absolute;left:93px;top:14px;font-family:"Oswald",sans-serif;font-weight:300;color:var(--ink);line-height:1}
.brand .l1{font-size:20px;display:block;white-space:nowrap}
.brand .l2{font-size:30px;letter-spacing:3px;display:block;margin-top:3px}
.cart{position:absolute;left:696px;top:10px;height:28px;display:flex}
.cart .lbl{background:var(--orange);color:#fff;font-family:"Oswald",sans-serif;font-weight:300;font-size:14px;
  padding:0 8px;display:flex;align-items:center;gap:7px;width:116px;white-space:nowrap;line-height:1}
.cart .drop{width:23px;background:#111;display:flex;align-items:center;justify-content:center}
.search{position:absolute;left:648px;top:50px;width:187px;height:26px;background:#fff;border:1px solid #d6d6d6}
.search svg{position:absolute;right:6px;top:7px}
.search .sep{position:absolute;right:27px;top:3px;width:1px;height:18px;background:#e4e4e4}
.mainnav{position:absolute;left:93px;top:122px;width:743px;height:33px;background:var(--orange);display:flex}
.mainnav a{color:#fff;text-decoration:none;font-family:"Oswald",sans-serif;font-size:12.5px;white-space:nowrap;
  display:flex;align-items:center;justify-content:center;border-right:1px solid #d4561c}
.mainnav a:last-child{border-right:0;flex:1}
.sidebar{position:absolute;left:93px;top:165px;width:185px;height:261px;border:1px solid var(--line)}
.sidebar h2{height:32px;background:linear-gradient(#4a4a4a,#1c1c1c);color:#fff;font-family:"Oswald",sans-serif;
  font-weight:400;font-size:13px;letter-spacing:.5px;padding:8px 0 0 9px}
.sidebar li{list-style:none;height:28.6px;border-bottom:1px solid #e0e0e0;background:#f6f6f6;white-space:nowrap;
  font-family:"Oswald",sans-serif;font-weight:300;font-size:11px;color:#333;padding:7px 0 0 27px}
.sidebar li:last-child{border-bottom:0}
.hero{position:absolute;left:295px;top:165px;width:541px;height:261px;
  background:radial-gradient(circle at 60% 50%,var(--banner-a),var(--banner-b));overflow:hidden}
.hero .product{position:absolute;left:22px;top:28px;width:286px;height:222px;border-radius:8px;
  background:linear-gradient(135deg,#f05a22 0%,#e0521d 55%,#2a2a2a 100%)}
.hero h1{position:absolute;left:325px;top:40px;color:#fff;font-family:"Oswald",sans-serif;font-weight:400;
  font-size:29px;line-height:42px;white-space:nowrap;text-shadow:0 1px 2px rgba(0,0,0,.25)}
.hero .price{position:absolute;left:325px;top:128px;color:#222;font-family:"Oswald",sans-serif;font-size:30px}
.hero .shop{position:absolute;left:330px;top:177px;width:107px;height:34px;background:#1f1f1f;color:#fff;white-space:nowrap;
  font-family:"Oswald",sans-serif;font-size:17px;display:flex;align-items:center;justify-content:center}
.hero .dots{position:absolute;right:16px;bottom:12px;display:flex;gap:4px}
.hero .dots i{width:7px;height:7px;border-radius:50%;background:#ddd;border:1px solid #888}
.hero .dots i:first-child{background:#333}
.partners{position:absolute;left:93px;top:437px;width:743px;height:68px;border:1px solid var(--line);
  display:flex;align-items:center;justify-content:space-between;padding:0 20px}
.partners span{height:24px;border-radius:2px;background:#cfcfcf}
.card{position:absolute;width:170px;height:223px;border:1px solid var(--line);text-align:center}
.card .pic{width:110px;height:100px;margin:18px auto 0;border-radius:6px}
.card .name{font-size:9.5px;color:var(--grey);line-height:11.5px;margin-top:20px;white-space:nowrap}
.card .cost{font-family:"Oswald",sans-serif;color:var(--price);font-size:12.5px;margin-top:10px}
.card .add{display:inline-block;margin-top:10px;width:70px;height:24px;background:var(--green);color:#fff;white-space:nowrap;
  font-family:"Oswald",sans-serif;font-size:10.5px;line-height:24px}
.rule{position:absolute;left:3px;top:1005px;width:926px;height:2px;background:#e2e2e2}
.fcol{position:absolute;top:1022px}
.fcol h3{font-family:"Oswald",sans-serif;font-weight:300;font-size:12px;color:#333;margin-bottom:6px;white-space:nowrap}
.fcol li{list-style:none;font-size:9.5px;color:#555;line-height:18.5px;white-space:nowrap}
.email{width:186px;height:26px;border:1px solid #ccc;font-size:9.5px;color:#555;padding:6px 5px}
.submit{position:absolute;left:124px;top:55px;width:62px;height:26px;background:var(--orange);color:#fff;
  font-family:"Oswald",sans-serif;font-size:12px;display:flex;align-items:center;justify-content:center}
.social{position:absolute;left:19px;top:95px;display:flex;gap:4px}
.social i{width:35px;height:35px;border-radius:50%;background:#9a9a9a;display:block}
.footbar{position:absolute;left:0;top:1160px;width:929px;height:40px;background:var(--black);color:#fff;
  font-size:9.5px;display:flex;align-items:center;justify-content:center}
</style>
</head>
<body>
<nav class="topbar"><a href="#">MY ACCOUNT</a><a href="#">SHOPPING CART</a><a href="#">REGISTER</a><a href="#">SIGN IN</a></nav>

<header class="masthead">
  <div class="brand"><span class="l1">TORCHLINE SUPPLIES</span><span class="l2">AUSTRALIA</span></div>
  <div class="cart">
    <div class="lbl"><svg width="20" height="14" viewBox="0 0 20 14"><path d="M1 1h3l2 8h10l2-6H6" fill="none" stroke="#fff" stroke-width="1.5"/><circle cx="8" cy="12" r="1.3" fill="#fff"/><circle cx="15" cy="12" r="1.3" fill="#fff"/></svg><span>MY CART: 0</span></div>
    <div class="drop"><svg width="9" height="6"><path d="M0 0h9L4.5 6z" fill="#fff"/></svg></div>
  </div>
  <div class="search"><span class="sep"></span><svg width="11" height="11" viewBox="0 0 11 11"><circle cx="4.5" cy="4.5" r="3.3" fill="none" stroke="#bbb" stroke-width="1.3"/><path d="M7 7l3 3" stroke="#bbb" stroke-width="1.5"/></svg></div>
</header>

<nav class="mainnav">
  <a href="#" style="width:69px">HOME</a><a href="#" style="width:117px">NEW PRODUCTS</a><a href="#" style="width:90px">SPECIALS</a><a href="#" style="width:105px">MY ACCOUNT</a><a href="#" style="width:93px">VIEW CART</a><a href="#" style="width:101px">DISCOUNTS</a><a href="#" style="width:83px">COUPON</a><a href="#">CONTACT</a>
</nav>

<aside class="sidebar">
  <h2>SELECT CATEGORIES</h2>
  <ul><li>ARC WELDING</li><li>MIG WELDING</li><li>TIG WELDING</li><li>PLASMA CUTTING</li><li>GENERAL ACCESSORIES</li><li>TOOLS</li><li>SPECIALS</li><li>NEW PRODUCTS</li></ul>
</aside>

<section class="hero">
  <div class="product" role="img" aria-label="Orange wheeled arc welding machine"></div>
  <h1>ARC WELDING<br>FORGE MIG 180C</h1>
  <div class="price">$1,090.00</div>
  <div class="shop">SHOP NOW!</div>
  <div class="dots"><i></i><i></i><i></i></div>
</section>

<section class="partners" aria-label="Partner badges">
  <span style="width:66px"></span><span style="width:50px"></span><span style="width:82px"></span><span style="width:93px"></span><span style="width:60px"></span><span style="width:71px"></span><span style="width:59px"></span><span style="width:70px"></span><span style="width:79px"></span>
</section>

<div class="card" style="left:93px;top:519px"><div class="pic" role="img" aria-label="Orange cabinet arc welder" style="background:linear-gradient(#f26522,#c8461a)"></div><p class="name">Forge MIG 180C including<br>Harrowby Gloves</p><p class="cost">$1,090.00</p><span class="add">ADD TO CART</span></div>
<div class="card" style="left:283px;top:519px"><div class="pic" role="img" aria-label="Red portable welder with leads" style="background:linear-gradient(#d63a2a,#3a2a2a)"></div><p class="name">Forge MIG 180C including<br>Harrowby Gloves</p><p class="cost">$1,090.00</p><span class="add">ADD TO CART</span></div>
<div class="card" style="left:474px;top:519px"><div class="pic" role="img" aria-label="Orange wheeled welder with cables" style="background:linear-gradient(#f07a2a,#444)"></div><p class="name">Forge MIG 180C including<br>Harrowby Gloves</p><p class="cost">$1,090.00</p><span class="add">ADD TO CART</span></div>
<div class="card" style="left:666px;top:519px"><div class="pic" role="img" aria-label="Framed welder generator" style="background:linear-gradient(#e8642a,#2a2a2a)"></div><p class="name">Forge MIG 180C including<br>Harrowby Gloves</p><p class="cost">$1,090.00</p><span class="add">ADD TO CART</span></div>

<div class="card" style="left:93px;top:758px"><div class="pic" role="img" aria-label="Blue inverter welder" style="background:linear-gradient(#3f6fd8,#b8bcc4)"></div><p class="name">Forge MIG 180C including<br>Harrowby Gloves</p><p class="cost">$1,090.00</p><span class="add">ADD TO CART</span></div>
<div class="card" style="left:283px;top:758px"><div class="pic" role="img" aria-label="Yellow industrial welder" style="background:linear-gradient(#f2d428,#2a2a2a)"></div><p class="name">Forge MIG 180C including<br>Harrowby Gloves</p><p class="cost">$1,090.00</p><span class="add">ADD TO CART</span></div>
<div class="card" style="left:474px;top:758px"><div class="pic" role="img" aria-label="Orange and grey compact inverter" style="background:linear-gradient(90deg,#4a5560,#ef5a26)"></div><p class="name">Forge MIG 180C including<br>Harrowby Gloves</p><p class="cost">$1,090.00</p><span class="add">ADD TO CART</span></div>
<div class="card" style="left:666px;top:758px"><div class="pic" role="img" aria-label="Orange AC arc welder" style="background:linear-gradient(#f25a22,#d3461a)"></div><p class="name">Forge MIG 180C including<br>Harrowby Gloves</p><p class="cost">$1,090.00</p><span class="add">ADD TO CART</span></div>

<div class="rule"></div>

<div class="fcol" style="left:94px"><h3>INFORMATION</h3><ul><li>Privacy Notice</li><li>Conditions of Use</li><li>Contact Us</li><li>Site Map</li><li>Gift Certificate FAQ</li></ul></div>
<div class="fcol" style="left:270px"><h3>HELP</h3><ul><li>Help</li><li>New Visitors</li><li>FAQ</li><li>Quick Guide</li><li>Unsubsribe</li></ul></div>
<div class="fcol" style="left:456px"><h3>MY ACCOUNT</h3><ul><li>My Cart</li><li>Wishlist</li><li>Order Returns</li><li>Track Order</li><li>Signin</li></ul></div>
<div class="fcol" style="left:642px"><h3>NEWSLETTER SIGN UP</h3>
  <div class="email">Enter Email Addres</div>
  <div class="submit">SUBMIT</div>
  <div class="social" aria-label="Social links"><i></i><i></i><i></i><i></i></div>
</div>

<footer class="footbar">© 2013 torchlinesuppliesaustralia.com.au</footer>
</body>
</html>
```